Large Financial Advisory Firm Needs a Brochure!

We are looking for a modern and professional 4 page brochure for our Financial Advisory firm, Harbrook Counsel Group. I've attached multiple files to help with the completion of the design.
SIZE OF BROCHURE: 17 x 11 FLAT, 8.5 x 11 inch FOLDED
1. A PDF titled Design Brief will provide you with an overview of the project, the text to be included in the brochure and other misc. instructions.
2. Logo Files, you will need to incorporate our logo into the brochure design, I've attached all the files please select the images that suit your design.
3. Competitor Illustration - I've attached an image that needs to be included on the 2nd page (inside left cover of the brochure). You will need to incorporate the pros/cons of using our competitors and the advantages of using our firm. This is outlined in the Design Brief PDF.
NOTE: If possible please get rid of the blue sky in the illustration. Just use the buildings, the blue throws off the concept. I contacted the illustrator and am waiting for a design without the sky but it may not be ready in time so please delete it if possible.
- I like the Avenir fonts, 85 Heavy, 65 Medium and 45.

```html
<!DOCTYPE html>
<html lang="en">
<head>
<meta charset="utf-8">
<title>Our Team – Harbrook Counsel Group</title>
<link rel="stylesheet" href="https://fonts.googleapis.com/css2?family=Nunito+Sans:wght@400;600;700&display=swap">
<style>
  :root {
    --ink: #121314;
    --gold: #fdb913;
    --gold-soft: #fcc02a;
    --body-text: #e9e9e9;
    --heading: #f6b41a;
  }
  * { margin: 0; padding: 0; box-sizing: border-box; }
  html, body { width: 927px; height: 1200px; overflow: hidden; }
  body { font-family: "Nunito Sans", "Avenir", sans-serif; background: var(--ink); }
  .page {
    position: relative;
    width: 927px;
    height: 1200px;
    background: var(--ink);
    overflow: hidden;
  }
  .accent-band {
    position: absolute;
    top: 0; right: 0;
    width: 211px;
    height: 1200px;
    background: linear-gradient(180deg, var(--gold) 0%, var(--gold-soft) 100%);
  }
  .page-title {
    position: absolute;
    left: 128px; top: 60px;
    color: var(--heading);
    font-size: 27px;
    font-weight: 700;
    letter-spacing: 0.2px;
  }
  .member {
    position: absolute;
    left: 128px;
    width: 532px;
  }
  .member--first { top: 146px; }
  .member--second { top: 492px; }
  .member--third { top: 819px; }
  .member-name {
    color: var(--heading);
    font-size: 17.5px;
    font-weight: 700;
    line-height: 21px;
  }
  .member-role {
    color: var(--body-text);
    font-size: 15px;
    font-weight: 400;
    line-height: 19px;
    margin-bottom: 19px;
  }
  .member-bio {
    color: var(--body-text);
    font-size: 13px;
    line-height: 18px;
    text-align: justify;
    margin-bottom: 18px;
  }
  .member-bio:last-child { margin-bottom: 0; }
</style>
</head>
<body>
<main class="page">
  <div class="accent-band" aria-hidden="true"></div>

  <h1 class="page-title">Our Team</h1>

  <section class="member member--first">
    <h2 class="member-name">Martin Calloway, CFA, CPA</h2>
    <p class="member-role">Founder</p>
    <p class="member-bio">Martin works collaboratively with advisors to formulate successful transition plans. He brings creative insight and deep experience to this niche industry that is sorely lacking in both. Prior to his current role, Martin worked at Meridian Fund Partners where he rose quickly to Regional Director and developed relationships with advisors throughout the Western US. He loved his role at the firm, but became frustrated when some of his closest clients struggled to find the right partner for succession. He witnessed deals implode due to cultural, philosophical, and operational differences and in some cases firms gave up their succession search altogether. He founded Harbrook Counsel Group to make sure advisors find the succession partner they deserve.</p>
    <p class="member-bio">Martin earned a bachelor’s degree in Finance from Eastfield University. He is a Certified Public Accountant and a CFA Charterholder. Martin enjoys spending time with his wife Renata, traveling internationally, studying foreign languages, and staying active.</p>
  </section>

  <section class="member member--second">
    <h2 class="member-name">Grant Holloway, CFA</h2>
    <p class="member-role">Founder</p>
    <p class="member-bio">Grant has over ten years of experience in the financial services industry. Prior to joining Harbrook Counsel Group, he has served as Portfolio Manager and research analyst for various financial service companies, both large and small. Grant wears multiple hats for the organization: he leads the portfolio management team, oversees our operations staff and handles the technological integration between firms. He has been involved in multiple Advisor mergers and transitions and understands the challenges that firms face when looking for a succession partner. Grant grew up in Southern California and earned a BA from Ashmore University where he studied Public Policy, Economics and German. He holds the Chartered Financial Analyst (CFA) designation.</p>
    <p class="member-bio">Grant enjoys spending his coveted free time with his wife Claire and 4 young children. Grant’s hobbies include martial arts, reading, cooking, and taking interesting MOOC courses.</p>
  </section>

  <section class="member member--third">
    <h2 class="member-name">Owen Holloway</h2>
    <p class="member-role">Founder</p>
    <p class="member-bio">Owen brings over 10 years of M&amp;A experience to Harbrook Counsel Group. His expertise in deal structure, operational management, and corporate finance allow him to design customized succession plans for advisors. Owen is previously experienced in commercial finance, in 1998 he co-founded Keystone Capital Leasing; and serving as President and Managing Member, built a 100+ employee &amp; $35mm revenue equipment leasing company, which he sold in July 2008. Owen attended Westvale University and earned a Bachelor of Arts degree in English Literature while obtaining a minor in Economics and Communications.</p>
    <p class="member-bio">Owen and his wife Maren have 4 active young children. Owen’s hobbies include competing in triathlons throughout the United States, traveling, gourmet cooking, and spending time with family.</p>
  </section>
</main>
</body>
</html>
```